Restaurant needs a vertical banner for fried catfish

Our restaurant is looking for an eye-catching 78.75in. x 36in. vertical physical banner ad for our fried catfish. Photos for the fried catfish will be provided as a reference but we will also accept anything similar to the photo. We will be using the following as our receptacle: https://www.plankoria.example/banner-stand/retractable-banner-stands/
The design must incorporate the following flavor texts:
Fried Catfish
Always Fresh!
Made from Scratch
Hand-cut Fillets
The Best Catfish in Texas
Served with fries, hush puppies, and a 32oz fountain drink
Also available by the pound!
The final design should be creative, professional, and eye-catching for customers.
Updates
Colors
Designer to choose colors to be used in the design.
Requirements
Must have
- We are open to any and all design elements, albeit the 'flavor texts' should not overpower, but complement the fried catfish photo. 'Fried Catfish' can be used in lieu of a main title/logo.
Nice to have
- Transparent or textured backgrounds that can encompass any or all part of the banner such as a cutting board, shadows, abstract, etc to show depth are a plus.
- Use of vectors or objects such as ribbons or shapes to encapsulate the 'flavor texts' are also encouraged.

```html
<!DOCTYPE html>
<html lang="en">
<head>
<meta charset="utf-8">
<title>Fried Catfish – Vertical Banner</title>
<link rel="stylesheet" href="https://fonts.googleapis.com/css2?family=Yellowtail&family=Roboto:wght@400;700;900&display=swap">
<style>
  :root {
    --backdrop: #d4d4d4;
    --orange-light: #ef7d22;
    --orange-deep: #e44a24;
    --brown: #5a3516;
    --white: #ffffff;
    --food-gold: #e2a020;
    --food-amber: #c96a12;
    --food-fries: #f4d23a;
    --pound-red: #e54824;
  }
  * { margin: 0; padding: 0; box-sizing: border-box; }
  html, body {
    width: 1200px;
    height: 1044px;
    overflow: hidden;
    background: var(--backdrop);
  }
  .canvas {
    position: relative;
    width: 1200px;
    height: 1044px;
  }
  .banner {
    position: absolute;
    left: 380px;
    top: 20px;
    width: 440px;
    height: 1004px;
    display: block;
    box-shadow: 0 6px 18px rgba(0,0,0,0.18);
  }
  .title {
    font-family: "Yellowtail", cursive;
    font-size: 112px;
    fill: var(--white);
  }
  .section-heading {
    font-family: "Roboto", sans-serif;
    font-weight: 900;
    font-size: 50px;
    fill: var(--white);
  }
  .flavor-item {
    font-family: "Roboto", sans-serif;
    font-weight: 400;
    font-size: 16px;
    fill: var(--white);
  }
  .served-line {
    font-family: "Roboto", sans-serif;
    font-weight: 700;
    font-size: 15px;
    fill: var(--white);
  }
  .pound-line {
    font-family: "Roboto", sans-serif;
    font-weight: 700;
    font-size: 31px;
    fill: url(#pound-gradient);
  }
</style>
</head>
<body>
<main class="canvas">
  <svg class="banner" viewBox="0 0 575 1312" preserveAspectRatio="none" xmlns="http://www.w3.org/2000/svg" aria-labelledby="banner-title">
    <defs>
      <linearGradient id="top-gradient" x1="0" y1="0" x2="1" y2="0">
        <stop offset="0" stop-color="var(--orange-light)"/>
        <stop offset="1" stop-color="var(--orange-deep)"/>
      </linearGradient>
      <linearGradient id="bottom-gradient" x1="0" y1="0" x2="1" y2="0">
        <stop offset="0" stop-color="var(--orange-deep)"/>
        <stop offset="1" stop-color="var(--orange-light)"/>
      </linearGradient>
      <linearGradient id="food-gradient" x1="0" y1="0" x2="1" y2="1">
        <stop offset="0" stop-color="var(--food-gold)"/>
        <stop offset="0.55" stop-color="var(--food-amber)"/>
        <stop offset="1" stop-color="var(--food-fries)"/>
      </linearGradient>
      <linearGradient id="thumb-gradient" x1="0" y1="0" x2="0" y2="1">
        <stop offset="0" stop-color="#d9502c"/>
        <stop offset="0.4" stop-color="var(--food-gold)"/>
        <stop offset="1" stop-color="var(--food-fries)"/>
      </linearGradient>
      <linearGradient id="pound-gradient" x1="0" y1="0" x2="1" y2="0">
        <stop offset="0" stop-color="var(--pound-red)"/>
        <stop offset="1" stop-color="var(--orange-light)"/>
      </linearGradient>
    </defs>

    <!-- Base panels -->
    <rect class="panel-top" x="0" y="0" width="575" height="700" fill="url(#top-gradient)"/>
    <rect class="panel-bottom" x="0" y="700" width="575" height="612" fill="url(#bottom-gradient)"/>

    <!-- Upper swoosh bands -->
    <path class="swoosh-white-thin" d="M270,272 C380,236 470,214 575,212 L575,226 C470,230 380,250 270,272 Z" fill="var(--white)"/>
    <path class="band-white" d="M0,332 C200,290 380,232 575,236 L575,254 C380,254 200,300 0,372 Z" fill="var(--white)"/>
    <path class="band-brown" d="M0,370 C200,300 380,252 575,252 L575,272 C380,270 200,330 0,392 Z" fill="var(--brown)"/>

    <!-- Hero food photo area -->
    <path class="hero-photo" role="img" aria-label="Photo of golden fried catfish fillets with fries and hush puppies on a plate"
          d="M0,392 C200,330 380,270 575,272 L575,742 C380,745 200,820 0,862 Z" fill="url(#food-gradient)"/>

    <!-- Lower swoosh bands -->
    <path class="band-white" d="M0,860 C200,818 380,742 575,740 L575,756 C380,760 200,838 0,874 Z" fill="var(--white)"/>
    <path class="band-brown" d="M0,872 C200,836 380,756 575,754 L575,772 C380,776 200,852 0,888 Z" fill="var(--brown)"/>
    <path class="band-white" d="M0,886 C200,850 380,772 575,770 L575,800 C380,800 200,870 0,896 Z" fill="var(--white)"/>
    <path class="swoosh-white-thin" d="M0,906 C100,902 180,890 240,876 C180,896 100,912 0,918 Z" fill="var(--white)"/>

    <!-- Title -->
    <text id="banner-title" class="title" x="288" y="172" text-anchor="middle" textLength="460" lengthAdjust="spacingAndGlyphs">Fried Catfish</text>

    <!-- Flavor list -->
    <text class="section-heading" x="45" y="984">FLAVOR</text>
    <g class="flavor-list">
      <text class="flavor-item" x="48" y="1023">•&#160;&#160;Fried Catfish</text>
      <text class="flavor-item" x="48" y="1047">•&#160;&#160;Always Fresh!</text>
      <text class="flavor-item" x="48" y="1071">•&#160;&#160;Made from Scratch</text>
      <text class="flavor-item" x="48" y="1095">•&#160;&#160;Hand-cut Fillets</text>
      <text class="flavor-item" x="48" y="1119">•&#160;&#160;The Best Catfish in Texas</text>
    </g>

    <!-- Thumbnail photo circles -->
    <g class="thumb-large" role="img" aria-label="Photo of fried catfish fillets with fresh tomatoes and lemons">
      <circle cx="433" cy="962" r="92" fill="none" stroke="var(--white)" stroke-opacity="0.7" stroke-width="1.5"/>
      <circle cx="433" cy="962" r="80" fill="url(#thumb-gradient)" stroke="var(--white)" stroke-width="4"/>
    </g>
    <g class="thumb-small" role="img" aria-label="Photo of fried catfish fillets over fries">
      <circle cx="348" cy="1049" r="82" fill="url(#bottom-gradient)" stroke="var(--white)" stroke-opacity="0.7" stroke-width="1.5"/>
      <circle cx="348" cy="1049" r="70" fill="url(#food-gradient)" stroke="var(--white)" stroke-width="4"/>
    </g>

    <!-- Served-with line -->
    <text class="served-line" x="45" y="1164" textLength="485" lengthAdjust="spacingAndGlyphs">SERVED WITH FRIES, HUSH PUPPIES, AND A 32OZ FOUNTAIN DRINK</text>

    <!-- Bottom white panel -->
    <path class="swoosh-white-thin" d="M385,1208 C450,1196 510,1192 575,1192 L575,1202 C510,1202 450,1204 385,1208 Z" fill="var(--white)"/>
    <path class="panel-footer" d="M0,1236 C200,1222 400,1188 575,1204 L575,1312 L0,1312 Z" fill="var(--white)"/>
    <path class="footer-accent" d="M0,1238 C100,1234 170,1228 240,1218 C170,1234 100,1244 0,1248 Z" fill="var(--orange-deep)"/>
    <text class="pound-line" x="288" y="1290" text-anchor="middle" textLength="470" lengthAdjust="spacingAndGlyphs">ALSO AVAILABLE BY THE POUND!</text>
  </svg>
</main>
</body>
</html>
```